Brickline Kit - iPhone app for tradespeople - UI design

Brickline Kit is an iPhone app for tradespeople (builders, carpenters, electricians, etc) which provides a range of tools that will assist with typical tasks, such as the calculation of unit conversion and spatial/volumetric/electrical measurements. The application also makes use of instruments available in the smartphone device to provide useful tools such as a spirit level, compass and torch.

The product is a simple menu-based application consisting of a number of menu and function screens. Each menu item will navigate the user to the function screen applicable to that menu item. Each function screen will contain the necessary inputs and features for perform its stated function.

The user interface should be designed with the tradesperson user in mind and as such should be simple, intuitive and durable with respect to its usability, interface design and branding elements.

Target Market(s)

Tradespeople (builders, carpenters, electricians, etc)

Industry/Entity Type

Trade

Font styles to use
Sans Serif

Requirements
Must have
• Refer to attached wireframes document...
• - Simple design
• - Consistent layout and theme
• - Screens and icons
Should not have
• - Tacky 3D images and textured backgrounds

```html
<!DOCTYPE html>
<html lang="en">
<head>
<meta charset="utf-8">
<title>Brickline Kit – Spirit Level</title>
<link href="https://fonts.googleapis.com/css2?family=Lato:wght@300;400&display=swap" rel="stylesheet">
<style>
  :root {
    --bg-top: #ececec;
    --bg-bottom: #e2e2e2;
    --label: #6f6f6f;
    --screen-top: #0d2b66;
    --screen-mid: #0a66a8;
    --screen-bottom: #05a8e6;
    --ink: #ffffff;
    --ring: rgba(255,255,255,0.38);
    --line: rgba(255,255,255,0.85);
    --bubble: rgba(225,240,252,0.62);
    --dot-off: rgba(255,255,255,0.4);
    --lens: rgba(255,255,255,0.03);
  }
  * { margin: 0; padding: 0; box-sizing: border-box; }
  html, body { width: 1200px; height: 1000px; overflow: hidden; }
  body {
    position: relative;
    background: linear-gradient(var(--bg-top), var(--bg-bottom));
    font-family: "Lato", "Helvetica Neue", Arial, sans-serif;
  }
  .mode-label {
    position: absolute; top: 70px;
    font-weight: 300; font-size: 54px; color: var(--label);
    transform: translateX(-50%); letter-spacing: -0.5px;
  }
  .screen {
    position: absolute; top: 234px; width: 316px; height: 561px;
    background: linear-gradient(var(--screen-top), var(--screen-mid) 50%, var(--screen-bottom));
    color: var(--ink); overflow: hidden;
  }
  .screen-a { left: 77px; }
  .screen-b { left: 451px; }
  .screen-c { left: 821px; }
  .nav-bar {
    position: absolute; top: 25px; left: 0; right: 0; height: 18px;
    font-size: 13px; font-weight: 400;
  }
  .nav-back { position: absolute; left: 14px; display: flex; align-items: center; gap: 9px; }
  .nav-title { position: absolute; left: 50%; transform: translateX(-50%); white-space: nowrap; }
  .nav-help { position: absolute; right: 26px; }
  .level-art { position: absolute; inset: 0; }
  .level-art text { font-family: "Lato", "Helvetica Neue", Arial, sans-serif; fill: var(--ink); }
  .reading { font-weight: 300; font-size: 27px; }
  .sign { font-weight: 300; font-size: 24px; }
</style>
</head>
<body>
  <div class="mode-label" style="left:237px">2in1</div>
  <div class="mode-label" style="left:793px">Swipe</div>

  <!-- Combined view -->
  <section class="screen screen-a">
    <div class="nav-bar">
      <span class="nav-back"><svg width="9" height="16" viewBox="0 0 9 16"><path d="M8 1 1 8l7 7" fill="none" stroke="#fff" stroke-width="1.3"/></svg>Back</span>
      <span class="nav-title">Spirit Level</span>
      <span class="nav-help">Help</span>
    </div>
    <svg class="level-art" viewBox="0 0 316 561">
      <defs>
        <clipPath id="a-top"><circle cx="157" cy="187" r="106"/></clipPath>
        <clipPath id="a-htube"><rect x="0" y="161" width="316" height="51"/></clipPath>
        <clipPath id="a-bot"><circle cx="157" cy="427" r="106"/></clipPath>
        <clipPath id="a-vtube"><rect x="131" y="0" width="53" height="561"/></clipPath>
      </defs>
      <circle cx="157" cy="187" r="106" fill="var(--lens)" stroke="var(--ring)" stroke-width="5"/>
      <text class="reading" x="157" y="131" text-anchor="middle">0.9°</text>
      <g clip-path="url(#a-top)" stroke="var(--line)" stroke-width="1">
        <line x1="0" y1="161" x2="316" y2="161"/><line x1="0" y1="212" x2="316" y2="212"/>
        <line x1="114" y1="161" x2="114" y2="212"/><line x1="124" y1="161" x2="124" y2="212"/>
        <line x1="192" y1="161" x2="192" y2="212"/><line x1="202" y1="161" x2="202" y2="212"/>
      </g>
      <g clip-path="url(#a-htube)"><ellipse cx="178" cy="169" rx="31" ry="15" fill="var(--bubble)"/></g>
      <text class="sign" x="76" y="195" text-anchor="middle">−</text>
      <text class="sign" x="241" y="196" text-anchor="middle">+</text>

      <line x1="25" y1="306" x2="290" y2="306" stroke="rgba(255,255,255,0.6)" stroke-width="1"/>

      <circle cx="157" cy="427" r="106" fill="var(--lens)" stroke="rgba(160,220,250,0.6)" stroke-width="5"/>
      <g clip-path="url(#a-bot)" stroke="var(--line)" stroke-width="1">
        <line x1="131" y1="300" x2="131" y2="560"/><line x1="184" y1="300" x2="184" y2="560"/>
        <line x1="131" y1="381" x2="184" y2="381"/><line x1="131" y1="390" x2="184" y2="390"/>
        <line x1="131" y1="459" x2="184" y2="459"/><line x1="131" y1="468" x2="184" y2="468"/>
      </g>
      <g clip-path="url(#a-vtube)"><ellipse cx="171" cy="445" rx="14" ry="30" fill="var(--bubble)"/></g>
      <text class="sign" x="157" y="351" text-anchor="middle">+</text>
      <text class="sign" x="157" y="524" text-anchor="middle">−</text>
      <text class="reading" x="223" y="439" text-anchor="middle">-0.4°</text>
    </svg>
  </section>

  <!-- Horizontal page -->
  <section class="screen screen-b">
    <div class="nav-bar">
      <span class="nav-back"><svg width="9" height="16" viewBox="0 0 9 16"><path d="M8 1 1 8l7 7" fill="none" stroke="#fff" stroke-width="1.3"/></svg>Back</span>
      <span class="nav-title">Spirit Level</span>
      <span class="nav-help">Help</span>
    </div>
    <svg class="level-art" viewBox="0 0 316 561">
      <defs>
        <clipPath id="b-ring"><circle cx="159" cy="287" r="106"/></clipPath>
        <clipPath id="b-tube"><rect x="0" y="261" width="316" height="52"/></clipPath>
      </defs>
      <text class="reading" x="159" y="131" text-anchor="middle">0.9°</text>
      <circle cx="159" cy="287" r="106" fill="var(--lens)" stroke="var(--ring)" stroke-width="5"/>
      <g clip-path="url(#b-ring)" stroke="var(--line)" stroke-width="1">
        <line x1="0" y1="261" x2="316" y2="261"/><line x1="0" y1="313" x2="316" y2="313"/>
        <line x1="114" y1="261" x2="114" y2="313"/><line x1="124" y1="261" x2="124" y2="313"/>
        <line x1="192" y1="261" x2="192" y2="313"/><line x1="202" y1="261" x2="202" y2="313"/>
      </g>
      <g clip-path="url(#b-tube)"><ellipse cx="177" cy="271" rx="31" ry="16" fill="var(--bubble)"/></g>
      <text class="sign" x="76" y="296" text-anchor="middle">−</text>
      <text class="sign" x="239" y="297" text-anchor="middle">+</text>
      <circle cx="152" cy="511" r="3.5" fill="#fff"/>
      <circle cx="164" cy="511" r="3.5" fill="var(--dot-off)"/>
    </svg>
  </section>

  <!-- Vertical page -->
  <section class="screen screen-c">
    <div class="nav-bar">
      <span class="nav-back"><svg width="9" height="16" viewBox="0 0 9 16"><path d="M8 1 1 8l7 7" fill="none" stroke="#fff" stroke-width="1.3"/></svg>Back</span>
      <span class="nav-title">Spirit Level</span>
      <span class="nav-help">Help</span>
    </div>
    <svg class="level-art" viewBox="0 0 316 561">
      <defs>
        <clipPath id="c-ring"><circle cx="159" cy="287" r="106"/></clipPath>
        <clipPath id="c-tube"><rect x="133" y="0" width="52" height="561"/></clipPath>
      </defs>
      <text class="reading" x="162" y="131" text-anchor="middle">-0.4°</text>
      <circle cx="159" cy="287" r="106" fill="var(--lens)" stroke="var(--ring)" stroke-width="5"/>
      <g clip-path="url(#c-ring)" stroke="var(--line)" stroke-width="1">
        <line x1="133" y1="150" x2="133" y2="420"/><line x1="185" y1="150" x2="185" y2="420"/>
        <line x1="133" y1="243" x2="185" y2="243"/><line x1="133" y1="252" x2="185" y2="252"/>
        <line x1="133" y1="321" x2="185" y2="321"/><line x1="133" y1="330" x2="185" y2="330"/>
      </g>
      <g clip-path="url(#c-tube)"><ellipse cx="172" cy="306" rx="14" ry="30" fill="var(--bubble)"/></g>
      <text class="sign" x="159" y="212" text-anchor="middle">+</text>
      <text class="sign" x="159" y="383" text-anchor="middle">−</text>
      <circle cx="152" cy="511" r="3.5" fill="var(--dot-off)"/>
      <circle cx="164" cy="511" r="3.5" fill="#fff"/>
    </svg>
  </section>
</body>
</html>
```